Redesign current business card for food company

i would like to redesign my business card. our company is food company, our product range from chips, juices, milk and etc (mostly dried food stuff).
I want o keep same logo but , the rest is open to new design.
you can check at our website about our company www.torvikeats.com

Target Market(s)

most of food company

Industry/Entity Type

Business

Contact Information for Business Card

I want to keep more to blue color...

Colors
3176b5
abd036

Requirements
Must have
• our old logo
Nice to have
• we do not mind to have nice material on bus card in order to accomplish nice design. for example: using spot uv, embossed and etc.

```html
<!DOCTYPE html>
<html lang="en">
<head>
<meta charset="utf-8">
<title>Torvik Business Card</title>
<link href="https://fonts.googleapis.com/css2?family=Montserrat:wght@400;500;700&display=swap" rel="stylesheet">
<style>
  :root{
    --navy:#2f2f94;
    --navy-soft:#3b3ba6;
    --cyan:#1cb0d0;
    --white:#ffffff;
    --stage:#e9eaee;
    --ink-light:#4a4aa8;
  }
  *{box-sizing:border-box;margin:0;padding:0}
  html,body{width:1200px;height:900px;overflow:hidden}
  body{background:var(--stage);font-family:'Montserrat',sans-serif;position:relative}
  .card{position:absolute;left:280px;width:640px;height:366px;border-radius:22px;overflow:hidden;box-shadow:0 10px 30px rgba(0,0,0,.15)}
  .card-back{top:54px;background:var(--navy)}
  .card-front{top:480px;background:var(--white)}

  /* back */
  .back-mark{position:absolute;left:0;right:0;top:70px;text-align:center;font-weight:500;font-size:150px;letter-spacing:-4px;color:var(--navy-soft);line-height:1}
  .back-web{position:absolute;right:180px;bottom:30px;color:var(--white);font-size:16px;letter-spacing:.5px}
  .edge{position:absolute;left:0;right:0;bottom:0;height:10px;display:flex}
  .edge span{display:block;height:100%}
  .back-edge .left{width:60%;background:var(--white)}
  .back-edge .right{flex:1;background:var(--cyan)}
  .front-edge .left{width:60%;background:var(--navy)}
  .front-edge .right{flex:1;background:var(--cyan)}

  /* front */
  .brand{position:absolute;left:36px;top:78px;font-weight:700;font-size:72px;letter-spacing:-2px;color:var(--navy);line-height:1}
  .person{position:absolute;right:36px;top:36px;text-align:right}
  .person-name{font-weight:700;font-size:19px;color:var(--navy)}
  .person-role{font-size:14px;color:var(--cyan);margin-top:2px}
  .rule{position:absolute;left:34px;right:30px;top:92px;height:1.5px;background:var(--navy)}
  .rule-main{top:204px;left:34px;right:300px}
  .contacts{position:absolute;left:36px;top:216px;list-style:none}
  .contacts li{display:flex;align-items:center;gap:12px;font-size:15.5px;color:var(--navy);line-height:24px}
  .contacts svg{width:13px;height:13px;fill:var(--cyan);flex:none}
  .contacts .accent{color:var(--cyan)}
  .address{position:absolute;right:36px;bottom:36px;text-align:right;font-size:14.5px;color:var(--navy);line-height:21px}
</style>
</head>
<body>

<section class="card card-back" aria-label="Card back">
  <div class="back-mark">torvik</div>
  <div class="back-web">www.torvikeats.com</div>
  <div class="edge back-edge"><span class="left"></span><span class="right"></span></div>
</section>

<section class="card card-front" aria-label="Card front">
  <div class="brand">torvik</div>
  <div class="person">
    <div class="person-name">Daniel Hartono</div>
    <div class="person-role">President</div>
  </div>
  <div class="rule" style="left:300px;top:86px"></div>
  <div class="rule rule-main"></div>
  <ul class="contacts">
    <li><svg viewBox="0 0 24 24"><path d="M6.6 10.8a15 15 0 0 0 6.6 6.6l2.2-2.2c.3-.3.7-.4 1-.2 1.1.4 2.3.6 3.6.6.6 0 1 .4 1 1V20c0 .6-.4 1-1 1A17 17 0 0 1 3 4c0-.6.4-1 1-1h3.5c.6 0 1 .4 1 1 0 1.3.2 2.5.6 3.6.1.3 0 .7-.2 1z"/></svg>555 014 2288</li>
    <li><svg viewBox="0 0 24 24"><path d="M6 2h12v6H6zM3 9h18v9h-3v4H6v-4H3zm5 6v5h8v-5z"/></svg>555 014 2277</li>
    <li><svg viewBox="0 0 24 24"><path d="M7 1h10a2 2 0 0 1 2 2v18a2 2 0 0 1-2 2H7a2 2 0 0 1-2-2V3a2 2 0 0 1 2-2zm0 3v14h10V4zm5 15.5a1 1 0 1 0 0 2 1 1 0 0 0 0-2z"/></svg>555 019 4631</li>
    <li><svg viewBox="0 0 24 24"><path d="M2 5h20v14H2zm2 2v.5l8 5 8-5V7zm0 2.8V17h16V9.8l-8 5z"/></svg>daniel@torvikeats.com</li>
    <li><svg viewBox="0 0 24 24"><path d="M12 2a10 10 0 1 0 0 20 10 10 0 0 0 0-20zm6.9 9h-3a15 15 0 0 0-1.3-6A8 8 0 0 1 18.9 11zM12 4.1c.9 1.3 1.7 3.7 1.9 6.9h-3.8c.2-3.2 1-5.6 1.9-6.9zM9.4 5a15 15 0 0 0-1.3 6h-3A8 8 0 0 1 9.4 5zM5.1 13h3a15 15 0 0 0 1.3 6A8 8 0 0 1 5.1 13zm6.9 6.9c-.9-1.3-1.7-3.7-1.9-6.9h3.8c-.2 3.2-1 5.6-1.9 6.9zm2.6-.9a15 15 0 0 0 1.3-6h3a8 8 0 0 1-4.3 6z"/></svg>www.<span class="accent">torvikeats</span>.com</li>
  </ul>
  <div class="address">
    Torvik Enterprises Corp.<br>
    2140 W 5th St. Larkfield CA 91800
  </div>
  <div class="edge front-edge"><span class="left"></span><span class="right"></span></div>
</section>

</body>
</html>
```